A4 Tri-fold Brochure for Sedation Dentist Specialist Dr. Marlon and Sedation Dentistry.

I would like to create an A4 tri-fold brochure for our Dental Sedation Specialist Dr. Marlon Vesk. Please carefully select the most suitable highlights from his bio below.

This brochure has two parts. Highlighting what makes Dr. Marlon Vesk unique and trustworthy. Include a picture of him (attached). The second part is about sedation dentistry. All you need to know here: http://www.calmchairplex.com/how-does-sedation-dentistry-work

Avoid making it too wordy.

Meet Dr. Roh Dak Marlon Vesk, DDS

Inspired to Become a Dentist:
As a child, Dr. Marlon Vesk always felt stressed whenever he had to see a dentist. He knew that he wanted to become a dentist to help put patients completely at ease while they experienced quality dental care.

He is passionate about giving patients the healthy, beautiful smiles they deserve. “I find it fulfilling when I can see my patients’ beautiful smiles and how they can finally appreciate the joy of eating with a healthy set of teeth. However, what I love most about my job is the ability to provide a stress-free and comfortable experience at the dentist’s office, particularly for children, through sedation and general anesthesia.”

Educational Achievements:
Before becoming a dentist, Dr. Marlon Vesk earned his undergraduate degree at the Pellridge University of Northern Basin where he received a Bachelor of Medical Science Honor Specialization degree with distinction in biochemistry. He then completed his Doctor of Dental Surgery degree with honors at the Harwick Crest University. While there, he received the Elmer Drayce Medal in his class for outstanding achievement in anesthesia. He then pursued his three-year residency as well as a master’s degree in dental anesthesia at the Harwick Crest University.

So he can provide his patients with the latest in dentistry, Dr. Marlon Vesk enjoys pursuing additional knowledge, particularly in the areas of dental anesthesia as well as advanced technologies in dentistry. He is currently part of the Molar Horizon Circle study club and has enrolled in the Core Rootwork Mini- Residency Program. He also serves as a clinical instructor at the Plenvo Center at the Harwick Crest University.

Association Memberships:
In addition to his academic credentials, Dr. Marlon Vesk is a member of several associations:
The Vantley Board of Dental Surgeons of Quarrow (VBDSQ)
Dental Norvane Guild of Dental Anesthesia (NGDA)
Brisken Forum of Dental Anesthesia (BFDA)
Quarrow Dental Federation (QDF)
Outside the Practice

When he’s not at the practice, Dr. Marlon Vesk enjoys spending time with his wife Wren and their two poodles Pippa and Biscuit, who are spoiled rotten! “Wren and I love taking our dogs out on hikes and to the dog park on weekends. I also enjoy a wide range of activities from model building and playing the piano to soccer, gym and archery.” He stays fit by working out at the local Fitwell gym, and he likes to walk in Ashbury Lake Park and Dunmore Field Park.

Dr. Marlon Vesk considers himself to be a kid at heart. He is a big fan of superheroes and animated movies. “I get really excited about any upcoming superhero or Zentry Lumo movies. Till this day, I still collect superhero toy figures.”

He supports the BrightCot Foundation as well as the Quarrow League for the Protection of Animal Welfare (LPAW).

Experience outstanding dental care with our highly skilled dentist. Contact us today to schedule an appointment with Dr. Marlon Vesk! He speaks English, Cantonese, and Mandarin.

Target Market(s)

Mothers with young kids.

Industry/Entity Type

Dental

Font styles to use
Sans Serif

Requirements
Should not have
• Prices

```html
<!DOCTYPE html>
<html lang="en">
<head>
<meta charset="utf-8">
<title>Meet Dr. Roh Dak Marlon Vesk, DDS</title>
<link href="https://fonts.googleapis.com/css2?family=PT+Sans:ital,wght@0,400;0,700;1,400;1,700&family=Tinos:ital@1&display=swap" rel="stylesheet">
<style>
:root{
  --sky:#2a9de2;
  --sky-pale:#d5eefa;
  --heading-blue:#1f7cc4;
  --link-blue:#1f86cf;
  --navy:#1b2a5c;
  --ink:#2b2b2b;
  --white:#ffffff;
}
*{margin:0;padding:0;box-sizing:border-box}
html,body{width:1200px;height:927px;overflow:hidden;background:var(--white)}
body{font-family:"PT Sans",sans-serif;color:var(--ink)}
.brochure{position:relative;width:1200px;height:927px;overflow:hidden;background:var(--white)}
.panel{position:absolute;top:0;height:927px}
.panel--intro{left:0;width:403px;background:var(--sky-pale)}
.panel--credentials{left:403px;width:406px}
.panel--life{left:809px;width:391px}

.intro-band{position:absolute;left:0;top:0;width:403px;height:364px;background:var(--sky)}
.intro-title{position:absolute;left:30px;top:16px;color:var(--white);font-family:"Tinos",serif;font-style:italic;font-weight:400;line-height:1.15}
.intro-title .meet{display:block;font-size:22px}
.intro-title .name{display:block;font-size:26px}
.portrait{position:absolute;left:68px;top:91px;width:267px;height:306px;background:linear-gradient(180deg,#e6e4e0 0%,#cfd2d6 45%,#24304f 70%,#1e2947 100%)}

.section-heading{position:absolute;font-size:24px;font-weight:400;color:var(--heading-blue);line-height:1}
.rule{position:absolute;height:2px;background:var(--heading-blue)}
.copy{position:absolute;font-size:15.4px;line-height:21.8px}
.copy p+p{margin-top:20px}

.band{position:absolute;background:var(--sky)}

.member-list{list-style:none;margin-top:22px}
.member-list li{position:relative;padding-left:16px;margin-left:34px;margin-bottom:20px}
.member-list li::before{content:"";position:absolute;left:0;top:8px;width:6px;height:6px;border-radius:50%;background:var(--sky)}

.sedation-list{list-style:none;margin-top:10px}
.sedation-list li{position:relative;padding-left:16px;margin-left:14px;margin-bottom:8px}
.sedation-list li::before{content:"";position:absolute;left:0;top:8px;width:6px;height:6px;border-radius:50%;background:var(--sky)}

.kit-art{position:absolute;left:24px;top:23px;width:258px;height:197px;background:radial-gradient(ellipse at 60% 45%,#f4f4f4 0%,#e3e3e3 60%,#ffffff 100%)}

.cta{position:absolute;left:17px;top:608px;width:360px;font-size:19.5px;line-height:23px;font-weight:700;font-style:italic;color:var(--navy)}
.cta .langs{color:var(--link-blue)}
.call-label{position:absolute;left:30px;top:798px;font-size:26px;line-height:1;color:#222}
.phone{position:absolute;left:30px;top:822px;font-size:42px;line-height:1;color:#222;letter-spacing:1px}
.web{position:absolute;left:30px;top:866px;font-size:20px;line-height:1;color:var(--link-blue)}
</style>
</head>
<body>
<div class="brochure">

  <section class="panel panel--intro">
    <div class="intro-band"></div>
    <h1 class="intro-title"><span class="meet">Meet</span><span class="name">Dr. Roh Dak Marlon Vesk, DDS</span></h1>
    <div class="portrait" role="img" aria-label="Portrait of Dr. Marlon Vesk smiling in navy scrubs with a stethoscope"></div>
    <h2 class="section-heading" style="left:20px;top:455px">Inspired to Become a Dentist</h2>
    <div class="rule" style="left:0;top:483px;width:371px"></div>
    <div class="copy" style="left:20px;top:505px;width:364px">
      <p>As a child, Dr. Marlon Vesk always felt stressed at the dentist, so he chose to become one to put patients completely at ease. “What I love most about my job is the ability to provide a stress-free and comfortable experience, particularly for children, through sedation and general anesthesia.”</p>
    </div>
    <h2 class="section-heading" style="left:20px;top:668px">About Sedation Dentistry</h2>
    <div class="rule" style="left:0;top:696px;width:371px"></div>
    <div class="copy" style="left:20px;top:712px;width:364px">
      <p>Sedation uses gentle medication to help patients relax and feel safe during dental care.</p>
      <ul class="sedation-list">
        <li>Mild oral sedation to general anesthesia</li>
        <li>Ideal for anxious kids and adults</li>
        <li>Monitored by a dental anesthesiologist</li>
        <li>Relaxed visits, little memory of treatment</li>
      </ul>
    </div>
  </section>

  <section class="panel panel--credentials">
    <div class="band" style="left:0;top:0;width:406px;height:12px"></div>
    <h2 class="section-heading" style="left:21px;top:22px">Educational Achievements</h2>
    <div class="rule" style="left:0;top:55px;width:370px"></div>
    <div class="copy" style="left:21px;top:66px;width:356px">
      <p>Dr. Marlon Vesk earned a Bachelor of Medical Science with distinction in biochemistry at the Pellridge University of Northern Basin. He completed his Doctor of Dental Surgery with honors at the Harwick Crest University, receiving the Elmer Drayce Medal for outstanding achievement in anesthesia, followed by a three-year residency and a master’s degree in dental anesthesia.</p>
      <p>He is part of the Molar Horizon Circle study club, is enrolled in the Core Rootwork Mini- Residency Program, and serves as a clinical instructor at the Plenvo Center at the Harwick Crest University.</p>
    </div>
    <h2 class="section-heading" style="left:21px;top:570px">Association Memberships</h2>
    <div class="rule" style="left:0;top:601px;width:370px"></div>
    <div class="copy" style="left:21px;top:614px;width:360px">
      <p>In addition to his academic credentials, Dr. Marlon Vesk is a member of several associations:</p>
      <ul class="member-list">
        <li>The Vantley Board of Dental Surgeons of Quarrow (VBDSQ)</li>
        <li>Dental Norvane Guild of Dental Anesthesia (NGDA)</li>
        <li>Brisken Forum of Dental Anesthesia (BFDA)</li>
        <li>Quarrow Dental Federation (QDF)</li>
      </ul>
    </div>
    <div class="band" style="left:0;top:894px;width:406px;height:33px"></div>
  </section>

  <section class="panel panel--life">
    <div class="kit-art" role="img" aria-label="Illustration of a white tooth beside a first aid kit with a red cross"></div>
    <div class="band" style="left:0;top:230px;width:391px;height:14px"></div>
    <h2 class="section-heading" style="left:17px;top:263px">Outside the Practice</h2>
    <div class="rule" style="left:0;top:295px;width:370px"></div>
    <div class="copy" style="left:17px;top:306px;width:357px">
      <p>When he’s not at the practice, Dr. Marlon Vesk enjoys time with his wife Wren and their two spoiled poodles, Pippa and Biscuit. He loves hikes, model building, piano, soccer and archery, and walks in Ashbury Lake Park and Dunmore Field Park.</p>
      <p style="margin-top:10px">He supports the BrightCot Foundation as well as the Quarrow League for the Protection of Animal Welfare (LPAW).</p>
    </div>
    <p class="cta">Experience outstanding dental care with our highly skilled dentist. Contact us today to schedule an appointment with Dr. Marlon Vesk! <span class="langs">He speaks English, Cantonese, and Mandarin.</span></p>
    <p class="call-label">Call Us:</p>
    <p class="phone">000 000 0000</p>
    <p class="web">www.website.com</p>
    <div class="band" style="left:0;top:894px;width:391px;height:33px"></div>
  </section>

</div>
</body>
</html>
```